Calder Pizza - Takeout Menu Design

We are looking for a takeout menu design.
We are looking for a( 5" x 8.5" DOUBLE SIDED) flyer with our available pizza flavors
Must be easy to ready and not "busy"

Must include our logo (attached)
website: www.calderpizza.ca
address:
Fenwick Ridge Plaza
417, 318 9 Avenue SW
and the following details:
Visit our website for our complete appetizer, pasta, salad and catering menu.

Winner of this contest will also be offered to create a few print designs via printhive.

Please do not hesitate to ask any questions.

Target Market(s)

Business / Office clientele

Industry/Entity Type

Pizza place / specializing in corporate orders

Requirements
Must have
• Easy to read
Should not have
• Can not be busy or cluttered

```html
<!DOCTYPE html>
<html lang="en">
<head>
<meta charset="utf-8">
<title>Calder Pizza – Take-Out Menu</title>
<link rel="stylesheet" href="https://fonts.googleapis.com/css2?family=Barlow:wght@300;400;500&display=swap">
<style>
  :root {
    --backdrop: #d6d6d6;
    --card-black: #0d0d0d;
    --brand-red: #b3282d;
    --menu-red: #c2383c;
    --text-white: #f4f4f4;
    --text-soft: #cfcfcf;
    --leader-grey: #8a8a8a;
    --faint-art: #262626;
  }
  * { box-sizing: border-box; margin: 0; padding: 0; }
  html, body {
    width: 1200px; height: 1200px; overflow: hidden;
    background: var(--backdrop);
    font-family: "Barlow", "Helvetica Neue", Arial, sans-serif;
    color: var(--text-white);
  }
  .stage { position: relative; width: 1200px; height: 1200px; }

  .menu-card {
    position: absolute; top: 175px; width: 499px; height: 847px;
    background: var(--card-black); overflow: hidden;
    box-shadow: 0 4px 14px rgba(0,0,0,.25);
  }
  .menu-card--front { left: 85px; }
  .menu-card--back { left: 622px; }

  /* front side */
  .hero-art { position: absolute; left: 0; top: 0; width: 499px; height: 210px; }
  .brand-name {
    position: absolute; left: 34px; top: 214px;
    font-size: 31px; font-weight: 300; letter-spacing: 1px;
    color: var(--text-white); display: flex; align-items: center; gap: 10px;
  }
  .brand-dot { width: 12px; height: 12px; border-radius: 50%; background: var(--brand-red); }
  .menu-title { position: absolute; left: 34px; top: 278px; font-weight: 400; line-height: 1; }
  .menu-title__line1 { display: block; font-size: 35px; letter-spacing: .5px; }
  .menu-title__line2 { display: block; font-size: 45px; margin-top: 8px; letter-spacing: .5px; }
  .title-rule { position: absolute; left: 34px; top: 398px; width: 207px; height: 4px; background: var(--text-white); }

  .classic-list { position: absolute; left: 34px; top: 425px; width: 440px; list-style: none; }
  .classic-list li {
    display: grid; grid-template-columns: 282px 79px 79px;
    font-size: 17px; line-height: 20px; color: var(--menu-red); letter-spacing: .3px;
  }
  .section-heading {
    position: absolute; left: 34px; top: 604px;
    font-size: 23px; font-weight: 400; letter-spacing: .4px;
  }
  .specialty-list { position: absolute; left: 34px; top: 650px; width: 440px; list-style: none; }
  .specialty-list li {
    display: grid; grid-template-columns: 282px 79px 79px; height: 31px;
  }
  .item-name { font-size: 17px; line-height: 17px; letter-spacing: .3px; }
  .item-desc { display: block; font-size: 8.5px; line-height: 10px; color: var(--text-soft); }
  .item-price { font-size: 17px; line-height: 20px; }

  .menu-footer {
    position: absolute; left: 34px; top: 810px; width: 440px;
    font-size: 9.5px; line-height: 13px; color: var(--text-soft); letter-spacing: .2px;
  }

  /* back side */
  .back-art { position: absolute; inset: 0; }
  .full-list {
    position: absolute; left: 22px; top: 20px; width: 460px; height: 800px;
    list-style: none; display: flex; flex-direction: column; justify-content: space-between;
  }
  .full-list li { display: grid; grid-template-columns: 264px 79px 79px; }
  .full-list .item-head { display: flex; align-items: center; }
  .full-list .item-name { font-size: 16px; line-height: 17px; white-space: nowrap; }
  .leader {
    flex: 1; height: 1px; margin: 0 12px 0 8px;
    background: repeating-linear-gradient(90deg, var(--leader-grey) 0 12px, transparent 12px 22px);
  }
  .full-list .item-desc { font-size: 8.5px; line-height: 10px; max-width: 232px; }
  .full-list .item-price { font-size: 11px; line-height: 17px; color: var(--text-soft); }
  .full-list .item-price--span { grid-column: 2 / 4; white-space: nowrap; }
</style>
</head>
<body>
<main class="stage">

  <section class="menu-card menu-card--front" aria-label="Front: classic and specialty pizzas">
    <svg class="hero-art" viewBox="0 0 499 210" role="img" aria-label="Illustrated pizza with tomato slices and basil leaves, seen from above">
      <defs>
        <radialGradient id="pizzaTone" cx="50%" cy="0%" r="75%">
          <stop offset="0%" stop-color="#f2cf7a"/>
          <stop offset="75%" stop-color="#e8b45a"/>
          <stop offset="100%" stop-color="#c9772f"/>
        </radialGradient>
      </defs>
      <path d="M0 0 H499 V40 C470 140 380 205 250 205 C120 205 20 130 0 60 Z" fill="url(#pizzaTone)"/>
    </svg>

    <div class="brand-name"><span>CALDER PIZZA</span><span class="brand-dot"></span></div>

    <h1 class="menu-title">
      <span class="menu-title__line1">CLASSIC TAKE-OUT</span>
      <span class="menu-title__line2">PIZZA 8" &amp; 13"</span>
    </h1>
    <div class="title-rule"></div>

    <ul class="classic-list">
      <li><span>PEPPERONI &amp; MUSHROOM</span><span>$12.99</span><span>$30.95</span></li>
      <li><span>PEPPERONI</span><span>$11.99</span><span>$29.95</span></li>
      <li><span>HAWAIIAN</span><span>$12.99</span><span>$30.95</span></li>
      <li><span>BEEF &amp; MUSHROOM</span><span>$13.49</span><span>$32.95</span></li>
      <li><span>PEPPERONI &amp; HAM</span><span>$12.99</span><span>$30.95</span></li>
      <li><span>HAM &amp; MUSHROOM</span><span>$12.99</span><span>$30.95</span></li>
      <li><span>BEEF &amp; ONION</span><span>$13.49</span><span>$32.95</span></li>
      <li><span>CHEESE</span><span>$11.99</span><span>$29.95</span></li>
    </ul>

    <h2 class="section-heading">SPECIALTY TAKE-OUT PIZZA- 8" &amp; 13"</h2>
    <ul class="specialty-list">
      <li><span class="item-name">ALL MEAT<span class="item-desc">Pepperoni, Beef &amp; Smoked Ham &amp; Bacon</span></span><span class="item-price">$14.99</span><span class="item-price">$35.95</span></li>
      <li><span class="item-name">DOUBLE PEPPERONI<span class="item-desc">Loads of Pepperoni</span></span><span class="item-price">$13.49</span><span class="item-price">$32.95</span></li>
      <li><span class="item-name">HOT HONEY PEPPERONI<span class="item-desc">Double Pepperoni and drizzled with Hot Honey</span></span><span class="item-price">$14.49</span><span class="item-price">$34.95</span></li>
      <li><span class="item-name">HAWAIIAN HEAT<span class="item-desc">Smoked Ham, Pineapple and Banana Peppers</span></span><span class="item-price">$13.49</span><span class="item-price">$32.95</span></li>
      <li><span class="item-name">FOUR CHEESE<span class="item-desc">Mozzarella, Feta, Romano and Cheddar Cheese</span></span><span class="item-price">$13.49</span><span class="item-price">$32.95</span></li>
    </ul>

    <footer class="menu-footer">
      <p>Visit our website for our complete appetizer, pasta, salad and catering menu.</p>
      <p>www.calderpizza.ca &nbsp;·&nbsp; Fenwick Ridge Plaza, 417, 318 9 Avenue SW</p>
    </footer>
  </section>

  <section class="menu-card menu-card--back" aria-label="Back: full pizza list">
    <svg class="back-art" viewBox="0 0 499 847" aria-hidden="true">
      <circle cx="470" cy="300" r="330" fill="var(--faint-art)"/>
      <path d="M0 0 H10 C60 350 200 650 443 847 H0 Z" fill="var(--brand-red)"/>
    </svg>

    <ul class="full-list">
      <li><div><div class="item-head"><span class="item-name">MONTREAL</span><span class="leader"></span></div><span class="item-desc">Pepperoni &amp; Double Smoked Bacon</span></div><span class="item-price">$13.49</span><span class="item-price">$32.95</span></li>
      <li><div><div class="item-head"><span class="item-name">MONTREAL HEAT</span><span class="leader"></span></div><span class="item-desc">Pepperoni, Double Smoked Bacon &amp; Banana Peppers</span></div><span class="item-price">$13.99</span><span class="item-price">$33.95</span></li>
      <li><div><div class="item-head"><span class="item-name">SUPREME</span><span class="leader"></span></div><span class="item-desc">Pepperoni, Mushrooms &amp; Green Peppers</span></div><span class="item-price">$13.49</span><span class="item-price">$32.95</span></li>
      <li><div><div class="item-head"><span class="item-name">CANADIAN</span><span class="leader"></span></div><span class="item-desc">Pepperoni, Mushrooms &amp; Ham</span></div><span class="item-price">$13.49</span><span class="item-price">$32.95</span></li>
      <li><div><div class="item-head"><span class="item-name">BBQ CHICKEN</span><span class="leader"></span></div><span class="item-desc">Chicken Breast, Hickory BBQ Sauce &amp; Red Onions.</span></div><span class="item-price">$13.99</span><span class="item-price">$33.95</span></li>
      <li><div><div class="item-head"><span class="item-name">BBQ CHICKEN PLUS</span><span class="leader"></span></div><span class="item-desc">Chicken Breast, Hickory BBQ Sauce, Red Onions &amp; Cilantro</span></div><span class="item-price">$14.79</span><span class="item-price">$34.95</span></li>
      <li><div><div class="item-head"><span class="item-name">SPICY BBQ CHICKEN</span><span class="leader"></span></div><span class="item-desc">Chicken Breast, Hickory BBQ Sauce, Red Onions &amp; Banana Peppers</span></div><span class="item-price">$14.49</span><span class="item-price">$35.95</span></li>
      <li><div><div class="item-head"><span class="item-name">SWEET CHILI CHICKEN</span><span class="leader"></span></div><span class="item-desc">Chicken Breast, Pineapple, Red Onions &amp; Sweet Chili Sauce</span></div><span class="item-price">$14.49</span><span class="item-price">$35.95</span></li>
      <li><div><div class="item-head"><span class="item-name">CHICKEN CLUB</span><span class="leader"></span></div><span class="item-desc">Chicken Breast, Double Smoked Bacon, Red Onions and Tomatoes</span></div><span class="item-price">$14.79</span><span class="item-price">$35.95</span></li>
      <li><div><div class="item-head"><span class="item-name">ATHENEAN</span><span class="leader"></span></div><span class="item-desc">Chicken Breast, Spinach, Feta Cheese and Tomato</span></div><span class="item-price">$14.49</span><span class="item-price">$34.95</span></li>
      <li><div><div class="item-head"><span class="item-name">GREEK SUPREME</span><span class="leader"></span></div><span class="item-desc">Chicken Breast, Feta Cheese, Tomato, Green Pepper, Red Onions &amp; Black Olives</span></div><span class="item-price">$14.99</span><span class="item-price">$35.95</span></li>
      <li><div><div class="item-head"><span class="item-name">MEDITERRANEAN CHICKEN</span><span class="leader"></span></div><span class="item-desc">Seasoned Chicken Breast, Tomatoes, Red Onions and Feta Cheese</span></div><span class="item-price">$14.79</span><span class="item-price">$35.95</span></li>
      <li><div><div class="item-head"><span class="item-name">ORIGINAL SPINACH</span><span class="leader"></span></div><span class="item-desc">Spinach &amp; Feta Cheese</span></div><span class="item-price">$13.49</span><span class="item-price">$32.95</span></li>
      <li><div><div class="item-head"><span class="item-name">ZEUS</span><span class="leader"></span></div><span class="item-desc">Spinach, Feta Cheese and Tomatoes</span></div><span class="item-price">$13.95</span><span class="item-price">$33.95</span></li>
      <li><div><div class="item-head"><span class="item-name">GREEK</span><span class="leader"></span></div><span class="item-desc">Feta Cheese, Tomato, Green Peppers, Red Onions and Black Olives</span></div><span class="item-price">$13.99</span><span class="item-price">$33.95</span></li>
      <li><div><div class="item-head"><span class="item-name">VEGETARIAN</span><span class="leader"></span></div><span class="item-desc">Mushrooms, Tomatoes, Green Peppers and Black Olives</span></div><span class="item-price">$13.49</span><span class="item-price">$32.95</span></li>
      <li><div><div class="item-head"><span class="item-name">VEGGIE DELIGHT</span><span class="leader"></span></div><span class="item-desc">Mushrooms, Tomatoes, Green Peppers, Black Olives &amp; Onions</span></div><span class="item-price">$13.95</span><span class="item-price">$33.95</span></li>
      <li><div><div class="item-head"><span class="item-name">DELUXE</span><span class="leader"></span></div><span class="item-desc">Pepperoni, Mushrooms, Ham, Tomatoes, Green Peppers and Red Onions</span></div><span class="item-price">$13.95</span><span class="item-price">$33.95</span></li>
      <li><div><div class="item-head"><span class="item-name">CALDER SPECIAL</span><span class="leader"></span></div><span class="item-desc">Pepperoni, Mushrooms, Ham, Green Peppers and Black Olives</span></div><span class="item-price">$14.49</span><span class="item-price">$34.95</span></li>
      <li><div><div class="item-head"><span class="item-name">DILL PICKLE</span><span class="leader"></span></div><span class="item-desc">Crispy Dill Pickles, Fresh Dill with our cream based garlic sauce. Served with our without bacon.</span></div><span class="item-price">$14.49</span><span class="item-price">$34.95</span></li>
      <li><div><div class="item-head"><span class="item-name">BBQ PULLED PORK</span><span class="leader"></span></div><span class="item-desc">Pulled Pork, Red Onions, Red Peppers and Cilantro.</span></div><span class="item-price item-price--span">$13.49 $32.95 / $14.49 $35.95</span></li>
    </ul>
  </section>

</main>
</body>
</html>
```